Need simple and modern looking business card with all my information on one side and logo on the other side
Info :
Company name - VELMAR CONSTRUCTION LLC
Company addres- 418 harbor 87th. Dunmoor park ny 10352
Email- velmarllc@tridomail.Com
Company phone number 555-318-6094
Cell number- 555-742-0583
Web site - velmarllc.Com
My name Gerald tomasino

Target Market(s)

Construction , home improvement, remodeling

Industry/Entity Type

Construction

Contact Information for Business Card

It has to be moder but at the same time simple

Font styles to use
Sans Serif

Colors
0255a3
ffffff
000000
f78f20
b1b1b1
9d9d9d
1b1b1b
33a6d7
ec1f27

Requirements
Must have
• My logo on one side maybe with a some kind of background on the other side all my information
Nice to have
• Some kind of background pictures provided by you .PLEASE HAVE ACCOUNT WITH PIXELVAULT WILL NOT PAY ANY EXTRA FEES .
Should not have
• Any kind of hamer, nails,screws, helmets itp. Please do not copy the other designs come up with something new.

```html
<!DOCTYPE html>
<html lang="en">
<head>
<meta charset="utf-8">
<title>Velmar Construction LLC – Business Card</title>
<link href="https://fonts.googleapis.com/css2?family=Quicksand:wght@500;600;700&display=swap" rel="stylesheet">
<style>
  :root {
    --orange: #f78f20;
    --orange-light: #f9a53a;
    --ink: #1b1b1b;
    --ink-soft: #2a2a2a;
    --white: #ffffff;
    --stage: #e4e4e4;
    --grey: #9d9d9d;
  }
  * { box-sizing: border-box; margin: 0; padding: 0; }
  html, body {
    width: 1200px; height: 900px; overflow: hidden;
    background: var(--stage);
    font-family: "Quicksand", sans-serif;
  }
  .card {
    position: absolute; left: 250px;
    width: 700px; height: 400px;
    overflow: hidden;
    box-shadow: 0 10px 28px rgba(0,0,0,.25);
  }
  .card--logo { top: 35px; }
  .card--info { top: 470px; }
  .card__shapes { position: absolute; inset: 0; }

  /* logo side */
  .brand {
    position: absolute; color: var(--white);
    font-weight: 700; line-height: 1; text-align: left;
  }
  .brand__name { display: block; font-size: 64px; letter-spacing: 3px; }
  .brand__sub { display: block; font-size: 19px; letter-spacing: 2.4px; margin-top: 4px; }
  .card--logo .brand { left: 70px; top: 125px; }
  .website {
    position: absolute; left: 400px; width: 190px; top: 362px;
    text-align: center; color: var(--white);
    font-size: 14px; font-weight: 600; letter-spacing: .5px;
  }

  /* contact side */
  .logo-box {
    position: absolute; left: 110px; top: 0; width: 230px; height: 140px;
    background: var(--ink);
  }
  .card--info .brand { left: 150px; top: 150px; color: var(--ink); }
  .card--info .brand__name { font-size: 40px; letter-spacing: 2px; }
  .card--info .brand__sub { font-size: 12.5px; letter-spacing: 1.6px; }

  .address {
    position: absolute; left: 455px; top: 48px;
    display: flex; align-items: flex-start; gap: 10px;
    color: var(--ink); font-size: 15px; font-weight: 600; line-height: 1.25;
  }
  .contact-panel {
    position: absolute; left: 430px; top: 175px; width: 240px; height: 175px;
    padding: 12px 14px;
  }
  .contact-panel__name {
    color: var(--ink); font-size: 19px; font-weight: 700; letter-spacing: .3px;
    margin-bottom: 16px;
  }
  .contact-list { list-style: none; }
  .contact-list li {
    display: flex; align-items: center; gap: 9px;
    color: var(--white); font-size: 13.5px; font-weight: 600;
    margin-bottom: 11px; white-space: nowrap;
  }
  .icon {
    flex: none; width: 20px; height: 20px; border-radius: 50%;
    background: var(--ink); display: flex; align-items: center; justify-content: center;
  }
  .icon svg { width: 11px; height: 11px; }
</style>
</head>
<body>

<section class="card card--logo" aria-label="Business card, logo side">
  <svg class="card__shapes" viewBox="0 0 700 400" width="700" height="400" aria-hidden="true">
    <rect width="700" height="400" fill="var(--orange)"/>
    <rect x="400" y="0" width="190" height="400" fill="var(--orange-light)"/>
    <polygon points="0,0 400,0 400,310 0,345" fill="var(--ink)"/>
    <polygon points="0,345 400,310 400,317 0,352" fill="var(--white)"/>
    <polygon points="590,0 700,0 700,250 590,262" fill="var(--ink-soft)"/>
    <polygon points="590,262 700,250 700,256 590,268" fill="var(--white)"/>
  </svg>
  <div class="brand">
    <span class="brand__name">VELMAR</span>
    <span class="brand__sub">CONSTRUCTION LLC</span>
  </div>
  <p class="website">velmarllc.Com</p>
</section>

<section class="card card--info" aria-label="Business card, contact side">
  <svg class="card__shapes" viewBox="0 0 700 400" width="700" height="400" aria-hidden="true">
    <rect width="700" height="400" fill="var(--ink)"/>
    <polygon points="0,0 700,0 700,150 0,310" fill="var(--orange)"/>
    <polygon points="0,310 700,150 700,157 0,317" fill="var(--white)"/>
    <rect x="430" y="175" width="240" height="175" fill="var(--orange)"/>
  </svg>

  <div class="logo-box"></div>
  <div class="brand">
    <span class="brand__name">VELMAR</span>
    <span class="brand__sub">CONSTRUCTION LLC</span>
  </div>

  <div class="address">
    <span class="icon">
      <svg viewBox="0 0 12 12"><path d="M6 1a3.2 3.2 0 0 0-3.2 3.2C2.8 6.6 6 11 6 11s3.2-4.4 3.2-6.8A3.2 3.2 0 0 0 6 1zm0 4.4a1.2 1.2 0 1 1 0-2.4 1.2 1.2 0 0 1 0 2.4z" fill="var(--orange)"/></svg>
    </span>
    <p>418 harbor 87th.<br>Dunmoor park ny 10352</p>
  </div>

  <div class="contact-panel">
    <p class="contact-panel__name">Gerald tomasino</p>
    <ul class="contact-list">
      <li>
        <span class="icon"><svg viewBox="0 0 12 12"><rect x="3.5" y="1" width="5" height="10" rx="1" fill="none" stroke="var(--orange)" stroke-width="1.2"/><circle cx="6" cy="9.3" r=".6" fill="var(--orange)"/></svg></span>
        555-742-0583
      </li>
      <li>
        <span class="icon"><svg viewBox="0 0 12 12"><path d="M3 1.5l1.8 2.2-1 1.2a6 6 0 0 0 3.3 3.3l1.2-1L10.5 9 9.3 10.5C5.2 10.3 1.7 6.8 1.5 2.7z" fill="var(--orange)"/></svg></span>
        555-318-6094
      </li>
      <li>
        <span class="icon"><svg viewBox="0 0 12 12"><rect x="1.5" y="3" width="9" height="6" fill="none" stroke="var(--orange)" stroke-width="1.1"/><path d="M1.5 3L6 6.5 10.5 3" fill="none" stroke="var(--orange)" stroke-width="1.1"/></svg></span>
        velmarllc@tridomail.Com
      </li>
    </ul>
  </div>
</section>

</body>
</html>
```